Glow in the Dark Inks Sales Flyer - Targeted to the music industry

We need help!
We need a creative flyer to tell the music industry about our new, colorful glow in the dark inks that look amazing on T-shirts and concert merchandise.

The flyer will go to merchandising managers for bands around the world. The design needs to be hip and contemporary but not offensive. No f-bombs please! Size is 4” x 6” or 3” x 5”, and will be printed on card stock. Design can be both sides if you want. We expect color but black and white with some fluorescent accents could be cool. Surprise us.
Here’s some copy, and we can fill in the contact info when the design is close to final.

Help your fans get lit with branded T-shirts and merchandise that glows in the dark!

Let our new Starwell Pigments light up your next show!

Call us now –
Updates

Hello Designers.

Please keep in mind that although the thought of glow-in-the-dark may trigger a glowing, green color in your creative minds, StarWell Pigments has a wide variety of colors to bring to offer. So please be sure to show that it's not only green glow we are promoting but we have a wide range of colors that glow (including pink, purple, white that glow blue, blue, green, orange, yellow, etc.)

Thank you!

```html
<!DOCTYPE html>
<html lang="en">
<head>
<meta charset="utf-8">
<title>Starwell Pigments – Glow Out Your Show</title>
<link rel="stylesheet" href="https://fonts.googleapis.com/css2?family=Comfortaa:wght@300;400;700&family=Fredoka:wght@500;700&display=swap">
<style>
  :root {
    --paper: #ffffff;
    --ink-black: #141414;
    --hot-pink: #e5157d;
    --lilac: #a04aa8;
    --silver: #c9c9c9;
    --cyan: #2bb3e6;
    --white: #ffffff;
    --label: #8a8a8a;
  }
  * { box-sizing: border-box; margin: 0; padding: 0; }
  html, body {
    width: 1200px; height: 1174px; overflow: hidden;
    background: var(--paper);
  }
  .canvas { position: relative; width: 1200px; height: 1174px; }

  .side-label {
    position: absolute;
    font-family: "Comfortaa", sans-serif;
    font-size: 22px; color: var(--label);
  }
  .side-label--front { left: 350px; top: 228px; }
  .side-label--back  { left: 688px; top: 492px; }

  .card { position: absolute; overflow: hidden; }
  .card__art { position: absolute; inset: 0; width: 100%; height: 100%; }

  /* Front */
  .card--front { left: 218px; top: 300px; width: 325px; height: 472px; }
  .front-name {
    position: absolute; left: 12px; top: 72px; width: 310px;
    font-family: "Fredoka", sans-serif; font-weight: 700;
    color: var(--lilac); line-height: 0.78; white-space: nowrap;
  }
  .front-name__line { display: block; font-size: 86px; letter-spacing: -2px; }
  .front-name__line--second { padding-left: 42px; }
  .front-name__line--third { padding-left: 130px; font-size: 38px; letter-spacing: 0; }

  .front-tagline {
    position: absolute; left: 14px; top: 312px; width: 305px;
    font-family: "Comfortaa", sans-serif; font-weight: 300;
    line-height: 0.85; color: var(--white); white-space: nowrap;
  }
  .front-tagline__row { display: block; }
  .front-tagline__glow { color: var(--ink-black); font-size: 58px; letter-spacing: -2px; }
  .front-tagline__out { font-size: 48px; }
  .front-tagline__your { display: block; padding-left: 128px; font-size: 48px; }
  .front-tagline__show { display: block; padding-left: 10px; font-size: 68px; color: var(--silver); letter-spacing: -2px; }

  /* Back */
  .card--back { left: 689px; top: 540px; width: 488px; height: 313px; }
  .back-name {
    position: absolute; left: 12px; top: 14px;
    font-family: "Fredoka", sans-serif; font-weight: 700;
    color: var(--ink-black); line-height: 0.75; white-space: nowrap;
  }
  .back-name__line { display: block; font-size: 64px; letter-spacing: -2px; }
  .back-name__line--second { padding-left: 120px; }
  .back-name__line--third { padding-left: 250px; font-size: 30px; letter-spacing: 0; }
  .back-name__dot {
    position: absolute; left: 150px; top: 4px;
    width: 10px; height: 10px; border-radius: 50%; background: var(--cyan);
  }
  .back-copy {
    position: absolute; left: 95px; top: 222px; width: 360px;
    transform: rotate(-12deg); transform-origin: left top;
    font-family: "Comfortaa", sans-serif; white-space: nowrap;
  }
  .back-copy__pitch { color: var(--white); font-size: 12.5px; font-weight: 400; line-height: 1.3; }
  .back-copy__call {
    margin-top: 2px; padding-left: 30px;
    color: var(--hot-pink); font-family: "Fredoka", sans-serif; font-weight: 700;
    font-size: 13px; line-height: 1.3;
  }
  .back-copy__show {
    padding-left: 130px;
    color: var(--white); font-family: "Fredoka", sans-serif; font-weight: 700;
    font-size: 30px; line-height: 1.05;
  }
  .back-contact-strip {
    position: absolute; right: 26px; bottom: 34px;
    width: 92px; height: 14px; background: var(--silver); opacity: 0.6;
  }
</style>
</head>
<body>
<main class="canvas">

  <span class="side-label side-label--front">recto</span>

  <section class="card card--front" aria-label="Front of flyer">
    <svg class="card__art" viewBox="0 0 325 472" preserveAspectRatio="none" aria-hidden="true">
      <defs>
        <linearGradient id="front-glow" x1="0" y1="0" x2="0.2" y2="1">
          <stop offset="0" stop-color="#8a3b9a"/>
          <stop offset="0.45" stop-color="#b53a9c"/>
          <stop offset="0.75" stop-color="#e5157d"/>
          <stop offset="1" stop-color="#c9b8c4"/>
        </linearGradient>
        <linearGradient id="front-night" x1="0" y1="0" x2="0" y2="1">
          <stop offset="0" stop-color="#141414"/>
          <stop offset="1" stop-color="#2a1630"/>
        </linearGradient>
      </defs>
      <rect width="325" height="472" fill="url(#front-night)"/>
      <polygon points="0,310 325,240 325,472 0,472" fill="url(#front-glow)"/>
      <polygon points="14,22 88,14 14,40" fill="#ffffff"/>
    </svg>
    <h1 class="front-name">
      <span class="front-name__line">star</span>
      <span class="front-name__line front-name__line--second">well</span>
      <span class="front-name__line front-name__line--third">pigments</span>
    </h1>
    <p class="front-tagline">
      <span class="front-tagline__row"><span class="front-tagline__glow">glow</span><span class="front-tagline__out">out</span></span>
      <span class="front-tagline__your">your</span>
      <span class="front-tagline__show">show</span>
    </p>
  </section>

  <span class="side-label side-label--back">verso</span>

  <section class="card card--back" aria-label="Back of flyer">
    <svg class="card__art" viewBox="0 0 488 313" preserveAspectRatio="none" aria-hidden="true">
      <defs>
        <linearGradient id="back-glow" x1="0" y1="0" x2="0.3" y2="1">
          <stop offset="0" stop-color="#e5157d"/>
          <stop offset="0.6" stop-color="#ee5aa4"/>
          <stop offset="1" stop-color="#f3a0c8"/>
        </linearGradient>
        <linearGradient id="back-night" x1="0" y1="0" x2="1" y2="1">
          <stop offset="0" stop-color="#1c1c1c"/>
          <stop offset="1" stop-color="#3a3a3a"/>
        </linearGradient>
      </defs>
      <rect width="488" height="313" fill="url(#back-glow)"/>
      <polygon points="0,290 488,150 488,313 0,313" fill="url(#back-night)"/>
      <polygon points="30,300 52,196 60,296" fill="#ffffff"/>
    </svg>
    <span class="back-name__dot" aria-hidden="true"></span>
    <h2 class="back-name">
      <span class="back-name__line">star</span>
      <span class="back-name__line back-name__line--second">well</span>
      <span class="back-name__line back-name__line--third">pigments</span>
    </h2>
    <div class="back-copy">
      <p class="back-copy__pitch">help your fans get lit with branded t-shirts<br>and merchandise that glows in the dark!</p>
      <p class="back-copy__call">let our new Starwell Pigments light up your</p>
      <p class="back-copy__show">next show!</p>
    </div>
    <div class="back-contact-strip" role="img" aria-label="Small decorative pattern strip"></div>
  </section>

</main>
</body>
</html>
```